bird wings, breathing, coaching, rhythm, heart

I would like this card design to be inspired by the following Rumi poem - now that I see some cards with the poem on it, I am pretty sure I don't want that. The feel of the cards should be watery and emotional, one of rhythm, breathing like a pendulum. An Ouroboros, (alchemical imagery in general), Birds, lungs, bird wings, hands, clouds, water, waves and rivers are all good images. Simple elegance is appreciated.
Cards should contain my name, title (coach), address, phone number and email address.
Your grief for what you've lost lifts a mirror
up to where you're bravely working.
Expecting the worst, you look, and instead,
here's the joyful face you've been wanting to see.
Your hand opens and closes and opens and closes.
If it were always a fist or always stretched open,
you would be paralyzed.
Your deepest presence
is in every small contracting and expanding,
the two as beautifully balanced and coordinated
as birdwings.
Contact Information for Business Card
Torven Maddick, MA
Coach
4817 Quarry Ln.
Alderton, CA 95821
415-382-6194
maddick@postvine.net
Colors
Designer to choose colors to be used in the design.
Look and feel

```html
<!DOCTYPE html>
<html lang="en">
<head>
<meta charset="utf-8">
<title>Torven Maddick, MA — Coach — Business Card</title>
<link rel="stylesheet" href="https://fonts.googleapis.com/css2?family=EB+Garamond:ital,wght@0,400;1,400&family=Roboto:wght@400&display=swap">
<style>
  :root {
    --backdrop: #2a2d31;
    --card-white: #fdfdfd;
    --ink: #1e1e1e;
    --rule: #3a3a3a;
    --sky-light: #d9ecec;
    --sea-mid: #a5d3d3;
    --sea-deep: #6bb7b9;
    --bird-grey: #5a5a5a;
  }
  html, body {
    margin: 0;
    width: 1200px;
    height: 900px;
    overflow: hidden;
    background: var(--backdrop);
  }
  .canvas {
    position: relative;
    width: 1200px;
    height: 900px;
  }
  .card {
    position: absolute;
    top: 296px;
    width: 540px;
    height: 309px;
    border-radius: 26px;
    overflow: hidden;
    box-shadow: 0 10px 30px rgba(0,0,0,0.35);
  }
  .card-front {
    left: 40px;
    background: var(--card-white);
    color: var(--ink);
  }
  .card-back {
    left: 620px;
  }
  .divider {
    position: absolute;
    left: 0;
    right: 0;
    top: 152px;
    height: 2px;
    background: var(--rule);
  }
  .name {
    position: absolute;
    left: 0;
    right: 0;
    top: 58px;
    padding-left: 110px;
    font-family: "EB Garamond", Georgia, serif;
    font-style: italic;
    font-size: 32px;
    line-height: 1;
    text-align: center;
    margin: 0;
    font-weight: 400;
  }
  .title {
    position: absolute;
    left: 0;
    right: 0;
    top: 98px;
    padding-left: 70px;
    font-family: "EB Garamond", Georgia, serif;
    font-size: 22px;
    line-height: 1;
    text-align: center;
  }
  .birds-on-line {
    position: absolute;
    left: 226px;
    top: 128px;
    width: 52px;
    height: 76px;
    border-radius: 8px;
    background: linear-gradient(180deg, var(--bird-grey) 0%, #8a8a8a 60%, rgba(160,160,160,0.2) 100%);
  }
  .address, .contact {
    position: absolute;
    font-family: "Roboto", Arial, sans-serif;
    font-size: 16px;
    line-height: 1.4;
    margin: 0;
    font-style: normal;
  }
  .address {
    left: 38px;
    top: 176px;
  }
  .contact {
    left: 330px;
    top: 224px;
    font-size: 18px;
  }
  .sea-sky {
    position: absolute;
    inset: 0;
    background:
      radial-gradient(ellipse 60% 30% at 60% 25%, rgba(255,255,255,0.85), rgba(255,255,255,0) 70%),
      linear-gradient(180deg, var(--sky-light) 0%, var(--sea-mid) 45%, var(--sea-deep) 100%);
  }
</style>
</head>
<body>
  <main class="canvas">
    <section class="card card-front">
      <div class="divider"></div>
      <h1 class="name">Torven Maddick, MA</h1>
      <div class="title">Coach</div>
      <div class="birds-on-line" role="img" aria-label="Ink illustration of small birds perched on the line"></div>
      <address class="address">4817 Quarry Ln.<br>Alderton, CA 95821</address>
      <p class="contact">415-382-6194<br>maddick@postvine.net</p>
    </section>
    <section class="card card-back">
      <div class="sea-sky" role="img" aria-label="Photograph of calm turquoise sea under soft white clouds"></div>
    </section>
  </main>
</body>
</html>
```